Distinctive Men collection for beard oil, beard balm and hand cream

I have a project: a collection for MEN.
The name of my company is KELV.
- You can play with the writing of the name without any problem.
- I need a label template for my BEARD oil bottles (it needs to have a place where I can change the skin type: dry skin / normal skin / or oily skin)
- I need a round label template for the 50 ml beard balm for the top of the aluminium can. I would like to use something similar for the hand cream so it would fit.

Example of Ingredients:
Beard oil | Oily skin: Ingrédients : Simmondsia chinensis (Jojoba) Seed Oil *, Corylus avellana (Hazelnut) Oil*, Vitis vinifera Seed Oil*, Trocopherol, parfum.

It is a collection, it needs to fit together!

Thank you :-D

Target Market(s)

MEN with a beard

Colors

Designer to choose colors to be used in the design.

Requirements
Must have
• - Labels for the bottles: 1 3/4' X 4'
• - Round label for the beard balm and the hand cream for men: round 1 3/4'
• - For the bottles: the ingredients goes on one end on the label and the Expiration on the other end, so they are "behind" the bottle. Hope I'm clear, I'm not a desgner ;-)
Nice to have
• I have been looking at labels type, and I like the effect of transparent label on amber buttle, BUT it is not at all a must. Just an observation. I am really open to everything!
Should not have
• Important fact: I don't want black and white like almost every bottles on Brindle and in barbershop. I want them both to appeal to trendy barbers AND I want them on Brindle.

```html
<!DOCTYPE html>
<html lang="en">
<head>
<meta charset="utf-8">
<title>KELV Beard Oil – Label Set</title>
<link rel="stylesheet" href="https://fonts.googleapis.com/css2?family=Poppins:wght@600;700&display=swap">
<style>
  :root {
    --page: #ffffff;
    --amber-dark: #6e2c08;
    --amber-mid: #a24b12;
    --amber-light: #c56d22;
    --ink: #ffffff;
    --dry: #e4dc2c;
    --normal: #8fd6a8;
    --oily: #6fd0dc;
  }
  * { margin: 0; padding: 0; box-sizing: border-box; }
  html, body {
    width: 1200px;
    height: 1000px;
    overflow: hidden;
    background: var(--page);
  }
  .label-set {
    width: 1200px;
    height: 1000px;
    display: flex;
    justify-content: center;
    align-items: center;
    gap: 60px;
  }
  .label {
    position: relative;
    width: 300px;
    height: 686px;
    border-radius: 14px;
    background: linear-gradient(90deg, var(--amber-dark) 0%, var(--amber-mid) 22%, var(--amber-light) 50%, var(--amber-mid) 78%, var(--amber-dark) 100%);
    overflow: hidden;
  }
  .label--dry { --accent: var(--dry); }
  .label--normal { --accent: var(--normal); }
  .label--oily { --accent: var(--oily); }

  .brand {
    position: absolute;
    left: 0;
    right: 0;
    top: 250px;
    display: flex;
    flex-direction: column;
    align-items: center;
    gap: 14px;
  }
  .brand__dot {
    width: 22px;
    height: 22px;
    border-radius: 50%;
    background: var(--accent);
  }
  .brand__name {
    font-family: "Poppins", sans-serif;
    font-weight: 700;
    font-size: 72px;
    line-height: 1;
    letter-spacing: 2px;
    color: var(--ink);
  }
  .product-name {
    position: absolute;
    left: 0;
    right: 0;
    top: 420px;
    text-align: center;
    font-family: "Poppins", sans-serif;
    font-weight: 600;
    font-size: 24px;
    letter-spacing: 4px;
    color: var(--ink);
  }
  .skin-rule {
    position: absolute;
    left: 0;
    right: 0;
    bottom: 170px;
    height: 2px;
    background: var(--accent);
  }
  .skin-type {
    position: absolute;
    left: 0;
    right: 0;
    bottom: 116px;
    text-align: center;
    font-family: "Poppins", sans-serif;
    font-weight: 600;
    font-size: 17px;
    letter-spacing: 1px;
    color: var(--ink);
  }
</style>
</head>
<body>
  <main class="label-set">
    <section class="label label--dry">
      <div class="brand">
        <span class="brand__dot"></span>
        <span class="brand__name">KELV</span>
      </div>
      <p class="product-name">BEARD OIL</p>
      <div class="skin-rule"></div>
      <p class="skin-type">DRY SKIN</p>
    </section>
    <section class="label label--normal">
      <div class="brand">
        <span class="brand__dot"></span>
        <span class="brand__name">KELV</span>
      </div>
      <p class="product-name">BEARD OIL</p>
      <div class="skin-rule"></div>
      <p class="skin-type">NORMAL SKIN</p>
    </section>
    <section class="label label--oily">
      <div class="brand">
        <span class="brand__dot"></span>
        <span class="brand__name">KELV</span>
      </div>
      <p class="product-name">BEARD OIL</p>
      <div class="skin-rule"></div>
      <p class="skin-type">OILY SKIN</p>
    </section>
  </main>
</body>
</html>
```